" Nós fazemos a administração geral dos condomínios. O que envolve solução de conflitos, contratação de serviços, orçamentos, administração financeira, reuniões de condôminos, relatórios gerenciais, orientações diversas ao síndico, conselheiros e condôminos. "

```html
<!DOCTYPE html>
<html lang="pt-BR">
<head>
<meta charset="UTF-8">
<title>Casalar Administradora — Pasta Institucional</title>
<link rel="stylesheet" href="https://fonts.googleapis.com/css2?family=Montserrat:wght@400;600&display=swap">
<style>
  :root {
    --backdrop: #c9cacc;
    --orange-light: #f6a623;
    --orange-deep: #e57f16;
    --sky-blue: #35aee6;
    --mid-blue: #1f7cc0;
    --deep-blue: #16548f;
    --photo-dark: #1d3a52;
    --photo-mid: #2d6b86;
    --photo-glow: #5fa9c9;
    --white: #ffffff;
  }
  * { margin: 0; padding: 0; box-sizing: border-box; }
  html, body {
    width: 1200px;
    height: 1200px;
    overflow: hidden;
    background: var(--backdrop);
    font-family: "Montserrat", sans-serif;
  }
  .folder {
    position: absolute;
    left: 120px;
    top: 260px;
    width: 960px;
    height: 680px;
    display: flex;
  }
  .panel {
    position: relative;
    width: 480px;
    height: 680px;
    overflow: hidden;
  }
  .panel--back {
    background: radial-gradient(circle at 35% 35%, var(--orange-light) 0%, var(--orange-deep) 100%);
  }
  .website {
    position: absolute;
    left: 120px;
    bottom: 46px;
    color: var(--white);
    font-size: 10px;
    font-weight: 400;
    letter-spacing: 0.5px;
    opacity: 0.9;
  }
  .panel--front {
    background: linear-gradient(180deg, var(--sky-blue) 0%, var(--mid-blue) 55%, var(--deep-blue) 100%);
  }
  .photo-band {
    position: absolute;
    left: 0;
    top: 150px;
    width: 480px;
    height: 210px;
    background:
      linear-gradient(180deg, rgba(95,169,201,0.55) 0%, rgba(45,107,134,0.3) 40%, rgba(29,58,82,0.85) 100%),
      linear-gradient(90deg, var(--photo-dark) 0%, var(--photo-mid) 50%, var(--photo-dark) 100%);
  }
  .brand {
    position: absolute;
    left: 0;
    width: 480px;
    top: 440px;
    text-align: center;
    color: var(--white);
  }
  .brand__mark {
    display: block;
    width: 22px;
    height: 22px;
    margin: 0 auto 10px;
    border-radius: 50%;
    background: var(--white);
  }
  .brand__name {
    font-size: 15px;
    font-weight: 600;
    letter-spacing: 1.5px;
    text-transform: uppercase;
  }
  .brand__tagline {
    margin-top: 4px;
    font-size: 6px;
    font-weight: 600;
    letter-spacing: 3px;
    text-transform: uppercase;
  }
</style>
</head>
<body>
  <main class="folder">
    <section class="panel panel--back">
      <p class="website">www.casalaradm.com.br</p>
    </section>
    <section class="panel panel--front">
      <div class="photo-band" role="img" aria-label="Fotografia noturna de um condomínio residencial iluminado"></div>
      <div class="brand">
        <span class="brand__mark"></span>
        <p class="brand__name">Casalar</p>
        <p class="brand__tagline">Administradora</p>
      </div>
    </section>
  </main>
</body>
</html>
```